Brindle Hollow Distilling needs a logo design

We need a logo design for Brindle Hollow Distilling based in Kelowna, B.C. The product name is "Gale Harbour Vodka" in a 750 ml bottle. Mountains, rivers, sunshine or whatever you think!

Size of label: approximately 5" high x 4" wide

Target Market(s)

19 - 35 year old

Industry/Entity Type

Product

Logo Text

Gale Harbour Vodka

Logo styles of interest
Character Logo
Requirements
Must have
• Gale Harbour Vodka, 750 ml, 40 % alc./vol. Return for refund where applicable(french also) Brindle Hollow Distilling, Dunmarrow, B.C. Canada T4K 8W3

```html
<!DOCTYPE html>
<html lang="en">
<head>
<meta charset="utf-8">
<title>Gale Harbour Vodka – Label</title>
<link rel="stylesheet" href="https://fonts.googleapis.com/css2?family=Big+Shoulders+Stencil+Display:wght@900&family=Crimson+Pro:wght@600&family=Philosopher:wght@700&display=swap">
<style>
  :root {
    --lime: #d8e226;
    --ink: #000000;
    --paper: #ffffff;
    --ring: #f3f1f3;
    --emblem-core: #e9d3a0;
    --emblem-mid: #6a2a18;
    --emblem-edge: #140806;
  }
  * { margin: 0; padding: 0; box-sizing: border-box; }
  html, body { width: 1200px; height: 960px; overflow: hidden; background: var(--lime); }
  .label { position: relative; width: 1200px; height: 960px; background: var(--lime); overflow: hidden; }
  .band-top, .band-bottom { position: absolute; left: 0; width: 100%; background: var(--lime); }
  .band-top { top: 0; height: 173px; }
  .band-bottom { top: 778px; height: 182px; }
  .panel-main { position: absolute; left: 0; top: 173px; width: 100%; height: 605px; background: var(--ink); }
  .product-name { position: absolute; left: 0; top: 200px; width: 1200px; height: 160px; margin: 0; }
  .product-name text {
    fill: var(--paper);
    font-family: "Big Shoulders Stencil Display", "Impact", sans-serif; font-weight: 900;
    font-size: 136px;
  }
  .emblem { position: absolute; left: 325px; top: 367px; width: 484px; height: 484px; }
  .abv {
    position: absolute; left: 30px; top: 734px; color: var(--paper);
    font-family: "Crimson Pro", "Times New Roman", serif; font-weight: 600;
    font-size: 27px; letter-spacing: -0.4px; white-space: nowrap;
  }
  .maker { position: absolute; left: 858px; top: 680px; width: 335px; height: 90px; }
  .maker text {
    fill: var(--paper);
    font-family: "Crimson Pro", "Times New Roman", serif; font-weight: 600;
    font-size: 25px;
  }
  .volume {
    position: absolute; left: 966px; top: 840px; color: var(--paper);
    font-family: "Philosopher", "Georgia", sans-serif; font-weight: 700;
    font-size: 56px; line-height: 1; letter-spacing: -1px; white-space: nowrap;
  }
</style>
</head>
<body>
  <main class="label">
    <div class="band-top"></div>
    <div class="panel-main"></div>
    <div class="band-bottom"></div>

    <svg class="product-name" viewBox="0 0 1200 160" role="heading" aria-level="1">
      <text x="600" y="142" text-anchor="middle" textLength="1080" lengthAdjust="spacingAndGlyphs">GALE HARBOUR VODKA</text>
    </svg>

    <svg class="emblem" viewBox="0 0 484 484" role="img" aria-label="Emblem artwork: glowing golden star in a dark circular badge">
      <defs>
        <radialGradient id="emblem-glow" cx="50%" cy="50%" r="50%">
          <stop offset="0%" stop-color="var(--emblem-core)"/>
          <stop offset="30%" stop-color="#a47a44"/>
          <stop offset="48%" stop-color="var(--emblem-mid)"/>
          <stop offset="60%" stop-color="#2a0e08"/>
          <stop offset="100%" stop-color="var(--emblem-edge)"/>
        </radialGradient>
      </defs>
      <circle cx="242" cy="242" r="234" fill="url(#emblem-glow)" stroke="var(--ring)" stroke-width="15"/>
    </svg>

    <p class="abv">40 % alc./vol</p>

    <svg class="maker" viewBox="0 0 335 90">
      <text x="2" y="33" textLength="325" lengthAdjust="spacingAndGlyphs">Brindle Hollow Distilling, Dunmarrow,</text>
      <text x="6" y="78">B.C. Canada T4K 8W3</text>
    </svg>

    <p class="volume">750 ml</p>
  </main>
</body>
</html>
```